Pro-life non-profit needs a dynamic poster design for their Christmas Gala.

We need a poster design which plays off the name of the event, The Winter Lantern. The Winter Lantern, of course is the Baby Jesus. Our cause supports unborn children in Iowa. The gala will include a concert of popular Christmas music sung by top soloists backed by an orchestra. An original commissioned song, The Winter Lantern, will be premiered. Purple and gold colors immediately come to mind, but a designer should not feel constrained on colors. We need an editable design w/fonts. Photoshop w/layers or Illustrator files are good.

```html
<!DOCTYPE html>
<html lang="en">
<head>
<meta charset="utf-8">
<title>The Winter Lantern – A Pro Life Christmas Gala</title>
<link rel="stylesheet" href="https://fonts.googleapis.com/css2?family=Lobster&family=Lato:wght@300&family=Fjalla+One&family=Raleway:wght@400&family=Prata&family=Playfair+Display:wght@700&family=Ultra&family=Special+Elite&display=swap">
<style>
  :root{
    --red:#c83d3f;
    --red-deep:#b83336;
    --gold:#d9b466;
    --white:#ffffff;
    --ink:#141010;
  }
  html,body{margin:0;padding:0;overflow:hidden;background:var(--red);}
  .poster{position:relative;width:845px;height:1200px;background:var(--red);overflow:hidden;color:var(--white);}
  .knit-band{position:absolute;left:0;width:845px;height:47px;background:var(--red-deep);}
  .knit-band.top{top:11px;}
  .knit-band.bottom{top:729px;}
  .heart-mark{position:absolute;left:406px;top:106px;width:37px;height:30px;background:rgba(255,255,255,.85);border-radius:4px;}
  .title{position:absolute;top:150px;left:0;width:845px;text-align:center;margin:0;
    font-family:"Lobster",cursive;font-weight:400;font-size:80px;line-height:1;color:var(--gold);}
  .subtitle{position:absolute;top:268px;left:0;width:845px;text-align:center;margin:0;
    font-family:"Lato",sans-serif;font-weight:300;font-size:28px;letter-spacing:1px;color:var(--white);}
  .dotted-rule{position:absolute;top:304px;left:255px;width:373px;border-top:2px dotted var(--gold);}
  .gold-band{position:absolute;left:0;width:845px;background:var(--gold);display:flex;align-items:center;justify-content:center;color:var(--red);}
  .program{top:335px;height:51px;font-family:"Fjalla One",sans-serif;font-size:34px;gap:12px;}
  .program .star{font-size:24px;}
  .info-row{position:absolute;top:410px;left:0;width:845px;height:46px;}
  .venue{position:absolute;right:566px;top:2px;text-align:right;font-family:"Raleway",sans-serif;font-size:14px;line-height:20px;}
  .divider{position:absolute;width:2px;background:rgba(217,180,102,.6);}
  .info-row .divider{top:7px;height:35px;}
  .date{position:absolute;left:323px;width:276px;top:4px;text-align:center;font-family:"Prata",serif;font-size:25px;color:var(--gold);}
  .doors{position:absolute;left:630px;top:6px;font-family:"Raleway",sans-serif;font-size:14px;line-height:20px;}
  .pricing{position:absolute;top:466px;left:0;width:845px;height:46px;font-family:"Playfair Display",serif;font-weight:700;font-size:32px;}
  .pricing .price-single{position:absolute;right:465px;top:0;}
  .pricing .price-table{position:absolute;left:430px;top:0;}
  .pricing .divider{left:402px;top:8px;height:36px;}
  .speaker{top:528px;height:50px;font-family:"Ultra",serif;font-size:21px;gap:14px;padding-left:20px;box-sizing:border-box;}
  .speaker .sep{font-size:18px;letter-spacing:1px;}
  .seating{position:absolute;top:608px;left:0;width:845px;text-align:center;margin:0;font-family:"Special Elite",monospace;font-size:27px;letter-spacing:1px;}
  .contact{position:absolute;left:0;width:845px;text-align:center;margin:0;font-family:"Prata",serif;color:var(--ink);font-size:23px;}
  .contact.tickets{top:654px;}
  .contact.lines{top:684px;}
  .photo{position:absolute;left:0;top:788px;width:845px;height:368px;
    background:radial-gradient(ellipse at 50% 45%,#f2a93a 0%,#a5642a 28%,#3a2a22 62%,#1c1b22 100%);}
  .dots{position:absolute;top:1173px;left:378px;display:flex;gap:14px;}
  .dots span{width:7px;height:7px;border-radius:50%;background:var(--gold);}
</style>
</head>
<body>
<main class="poster">
  <div class="knit-band top" role="img" aria-label="White knitted diamond pattern border"></div>
  <div class="heart-mark" role="img" aria-label="Small knitted heart ornament"></div>

  <h1 class="title">The Winter Lantern</h1>
  <p class="subtitle">A PRO LIFE CHRISTMES GALA</p>
  <div class="dotted-rule"></div>

  <div class="gold-band program">
    <span>Cocktail</span><span class="star">★</span><span>Dinner</span><span class="star">★</span><span>Christmes Concert</span>
  </div>

  <div class="info-row">
    <div class="venue">Maple Hall Center<br>W . Des Moines, IA</div>
    <div class="divider" style="left:323px"></div>
    <div class="date">November 21st, 2020</div>
    <div class="divider" style="left:599px"></div>
    <div class="doors">Door Open at<br>5 : 30 P.M.</div>
  </div>

  <div class="pricing">
    <span class="price-single">$ 60 person</span>
    <div class="divider"></div>
    <span class="price-table">$ 500 table of ten</span>
  </div>

  <div class="gold-band speaker">
    <span>Special Guest Speaker</span><span class="sep">:::::::</span><span>Bishop Thomas Halvorsen</span>
  </div>

  <p class="seating">Seating Limited ::: Reservations Needed</p>
  <p class="contact tickets">Order Tickets Online : www.HeartlandForLife.org</p>
  <p class="contact lines">515-555-0148&nbsp; events@heartlandforlife.org</p>

  <div class="knit-band bottom" role="img" aria-label="White knitted diamond pattern border"></div>

  <div class="photo" role="img" aria-label="Photo of lit yellow candles among pine greenery, red baubles and a small white Christmas house"></div>

  <div class="dots"><span></span><span></span><span></span><span></span><span></span><span></span></div>
</main>
</body>
</html>
```